依頼詳細
サイト構成・基本的な要件については
https://zumora.example/diagrams/P3TR8xmaqelu2sHb
を併せてご覧いただければ幸いです。
※導線が確保されていれば、必ずしもレイアウト案に忠実である必要はございません。
ぜひご提案いただければ幸甚です。

また、素材については
http://nibulo-share.example/download/58174a2c9d3e0b6f1a7c4e2d9b8f0a6c3e5d7b1f
よりダウンロードいただければと存じます。

上記だけで制作が難しい場合は
http://moruka.example/
などから、5000円程度までならこちらにて購入可能です。カンプデータにて作成頂き、
納品時に当方にて購入したデータに差し替えていただければと存じます。

全体的なデザインのイメージとしては

http://www.tovira-hatake.example/
http://www.samolet.example/rollmode/
http://vesmira.example/
http://ri-kogetsu.example/
のような、白ベースですっきりと見やすい印象が希望です。

メインカラーは既存サイトと同様、グリーンでお願いします。
http://www.tobakitchen.example/
サイトURL
ページ数
1ページ
希望イメージ
シンプル 複雑
単色 カラフル
暗い 明るい
日常 高級
遊び心 厳粛
未来的 伝統的
女性的 男性的
希望する色
白を基調とし、グリーンベースでスッキリと明るく見やすいデザインを希望します
納品ファイル
• 高解像度JPG (.jpg)
• フォトショップ形式 (.psd)
補足説明
素材については
よりダウンロードいただければと存じます。

上記だけで制作が難しい場合は
http://moruka.example/

白ベースでメインカラーは既存と同様にグリーンを使用し、
明るく見やすいデザインをお願いできればと思います。

http://bottom-parts.example/2012/166.html
http://bottom-parts.example/2011/115.html
→フッター部分の参照

基本レイアウト
については、必ずしも忠実である必要はありません。

是非ご提案お待ちしております。
何卒よろしくお願いいたします。

制作につきましてご不明な点がございましたら、お気軽にお申し付けいただければと存じます。
ご提案お待ちしております。

クライアント様との協議の結果こちらの案を採用させていただきました。
高級感と柔らかさのバランスがとてもよく、
視認性も高く、要望を全て満たしておりましたので
こちらの案を採用いたしました。

この度は多数ご提案いただきありがとうございました。
当選に至らなかったランサー様におかれましては大変心苦しいのですが、
またの機会にぜひご提案いただければ幸甚です。
引き続き何卒よろしくお願いいたします。

```html
<!DOCTYPE html>
<html lang="ja">
<head>
<meta charset="utf-8">
<title>トバキッチン | 料理教室</title>
<link rel="stylesheet" href="https://fonts.googleapis.com/css2?family=Noto+Sans+JP:wght@400;500;700&family=Noto+Serif+JP:wght@700;900&display=swap">
<style>
:root{
  --green:#6aa63c;
  --green-dark:#4f8a26;
  --green-light:#e9f3dc;
  --green-pale:#f4f9ee;
  --text:#444;
  --muted:#888;
  --line:#dcdcdc;
  --bg:#ffffff;
  --footer:#efeae2;
  --footer-bar:#6b5e4f;
  --accent:#e0781e;
  --red:#b8202a;
}
*{box-sizing:border-box;margin:0;padding:0}
html,body{width:759px;height:1200px;overflow:hidden;background:var(--bg)}
body{position:relative;font-family:"Noto Sans JP",sans-serif;color:var(--text);font-size:9px;line-height:1.4}
.abs{position:absolute}
.photo{position:absolute}

/* header */
.site-header{position:absolute;left:0;top:0;width:759px;height:96px;border-bottom:1px solid var(--line)}
.brand{position:absolute;left:18px;top:18px;display:flex;align-items:center;gap:8px}
.brand-mark{width:30px;height:30px;border-radius:50%;background:var(--green)}
.brand-name{font-size:22px;font-weight:500;color:var(--green-dark);line-height:1}
.brand-sub{font-size:8px;color:var(--green-dark);letter-spacing:.12em;margin-top:4px}
.school-links{position:absolute;left:300px;top:14px;display:flex;gap:10px;font-size:10px}
.school-links span{color:var(--text)}
.school-links i{font-style:normal;color:var(--line)}
.trial-btn{position:absolute;right:14px;top:8px;width:176px;height:30px;border-radius:4px;background:var(--green);color:#fff;font-size:10px;font-weight:700;display:flex;align-items:center;justify-content:center}
.global-nav{position:absolute;left:196px;top:50px;display:flex}
.global-nav li{list-style:none;width:108px;height:40px;border-left:1px solid var(--line);text-align:center;padding-top:6px}
.global-nav li:last-child{border-right:1px solid var(--line)}
.global-nav b{display:block;font-size:11px;font-weight:500;color:var(--text)}
.global-nav small{display:block;font-size:7px;color:var(--green);letter-spacing:.08em}

/* hero */
.hero{left:0;top:97px;width:759px;height:158px;background:linear-gradient(90deg,#d9c9a8 0%,#f3ece0 40%,#e7e1d4 70%,#b7a98f 100%)}
.hero-copy{position:absolute;left:300px;top:110px;width:240px;text-align:center}
.hero-copy h1{font-family:"Noto Serif JP",serif;font-weight:900;font-size:24px;color:var(--red);letter-spacing:.02em;line-height:1.2}
.hero-copy p{font-family:"Noto Serif JP",serif;font-weight:700;font-size:14px;color:#333;line-height:1.45;margin-top:6px}
.thumb-strip{position:absolute;left:0;top:258px;width:759px;height:22px;display:flex;gap:3px;justify-content:center;background:#f2f2f2}
.thumb-strip div{width:34px;height:22px;background:linear-gradient(#cbb89a,#9e8a6a)}

/* sidebar */
.sidebar{position:absolute;left:13px;top:288px;width:176px}
.trial-box{background:var(--green);color:#fff;border-radius:4px;padding:8px 10px;font-size:10px;font-weight:700;line-height:1.5}
.tel{margin-top:10px}
.tel dt{font-size:9px;color:var(--green-dark);font-weight:700}
.tel dd{display:flex;align-items:center;gap:5px;font-size:19px;font-weight:700;color:#333;line-height:1.2;margin-bottom:7px}
.side-nav{margin-top:12px;border-top:1px solid var(--line)}
.side-nav li{list-style:none;height:27px;border-bottom:1px solid var(--line);padding:6px 0 0 14px;font-size:9px;position:relative}
.side-nav li::before{content:"";position:absolute;left:4px;top:11px;border:3px solid transparent;border-left:4px solid var(--green)}
.side-btn{margin-top:8px;height:34px;border:1px solid var(--line);border-radius:3px;display:flex;align-items:center;gap:8px;padding-left:12px;font-size:10px;font-weight:700;color:var(--green-dark)}
.side-btn .dot{width:16px;height:16px;border-radius:50%;background:var(--green-light)}

/* main */
.sec-head{position:absolute;height:20px;background:var(--green);color:#fff;font-size:10px;font-weight:700;padding:3px 10px;border-radius:3px 3px 0 0}
.news{position:absolute;left:197px;top:308px;width:296px}
.news li{list-style:none;display:flex;gap:10px;border-bottom:1px dotted var(--line);padding:6px 4px;font-size:8px}
.news time{color:var(--muted);flex:none;width:62px}
.more{position:absolute;font-size:8px;color:var(--green-dark)}
.recipes{position:absolute;left:506px;top:308px;width:240px}
.recipe{display:flex;gap:6px;padding:6px 0;border-bottom:1px dotted var(--line);font-size:8px}
.recipe .photo{position:static;flex:none;width:52px;height:34px;background:linear-gradient(135deg,#d79b55,#8b5a2b)}

.cards{position:absolute;left:197px;top:508px;width:549px;display:grid;grid-template-columns:repeat(3,176px);gap:14px 10px}
.card{height:200px}
.card .photo{position:static;width:176px;height:128px}
.card h3{font-size:10px;font-weight:700;color:#333;margin:6px 0 3px;display:flex;align-items:center;gap:4px}
.card h3::before{content:"";width:7px;height:7px;background:var(--accent);border-radius:50%}
.card p{font-size:8px;color:var(--muted);line-height:1.5}

.pagetop{position:absolute;right:14px;top:940px;font-size:8px;color:var(--muted);letter-spacing:.1em}

/* footer */
.site-footer{position:absolute;left:0;top:972px;width:759px;height:228px;background:var(--footer)}
.footer-brand{position:absolute;left:40px;top:40px}
.footer-brand .brand-name{font-size:24px}
.home-btn{position:absolute;left:60px;top:108px;width:80px;height:20px;border-radius:10px;background:var(--green);color:#fff;font-size:8px;display:flex;align-items:center;justify-content:center}
.footer-nav{position:absolute;left:270px;top:40px;display:flex;gap:40px}
.footer-nav ul{list-style:none}
.footer-nav li{font-size:8px;margin-bottom:9px;padding-left:9px;position:relative}
.footer-nav li::before{content:"";position:absolute;left:0;top:3px;border:3px solid transparent;border-left:4px solid var(--green)}
.copyright{position:absolute;left:0;bottom:0;width:759px;height:26px;background:var(--footer-bar);color:#fff;font-size:8px;padding:7px 20px}
</style>
</head>
<body>

<header class="site-header">
  <div class="brand">
    <span class="brand-mark"></span>
    <div><div class="brand-name">トバキッチン</div><div class="brand-sub">TOBA KITCHEN SCHOOL</div></div>
  </div>
  <div class="school-links"><span>本町校</span><i>|</i><span>港町校</span><i>|</i><span>緑が丘校</span></div>
  <div class="trial-btn">体験レッスン・見学受付中！</div>
  <ul class="global-nav">
    <li><b>入会案内</b><small>ENTRY</small></li>
    <li><b>コース案内</b><small>COURSE</small></li>
    <li><b>料金表</b><small>PRICE</small></li>
    <li><b>よくあるご質問</b><small>Q&amp;A</small></li>
    <li><b>教室案内</b><small>SCHOOL</small></li>
  </ul>
</header>

<div class="photo hero" role="img" aria-label="パスタを持ち上げる手元と料理中のシェフの写真"></div>
<div class="hero-copy">
  <h1>実践こそが上達の近道！</h1>
  <p>簡単な家庭料理から<br>本格的な料理まで習得できる</p>
</div>
<div class="thumb-strip" role="img" aria-label="料理写真のサムネイル列">
  <div></div><div></div><div></div><div></div><div></div><div></div><div></div><div></div><div></div><div></div>
</div>

<aside class="sidebar">
  <div class="trial-box">体験レッスン・見学受付中！<br>各校舎にご連絡ください</div>
  <dl class="tel">
    <dt>本町校</dt>
    <dd><svg width="14" height="14" viewBox="0 0 24 24"><path fill="#6aa63c" d="M6.6 10.8a15 15 0 0 0 6.6 6.6l2.2-2.2a1 1 0 0 1 1-.25 11.4 11.4 0 0 0 3.6.57 1 1 0 0 1 1 1V20a1 1 0 0 1-1 1A17 17 0 0 1 3 4a1 1 0 0 1 1-1h3.5a1 1 0 0 1 1 1c0 1.25.2 2.45.57 3.57a1 1 0 0 1-.25 1z"/></svg>03-4120-7751</dd>
    <dt>港町校</dt>
    <dd><svg width="14" height="14" viewBox="0 0 24 24"><path fill="#6aa63c" d="M6.6 10.8a15 15 0 0 0 6.6 6.6l2.2-2.2a1 1 0 0 1 1-.25 11.4 11.4 0 0 0 3.6.57 1 1 0 0 1 1 1V20a1 1 0 0 1-1 1A17 17 0 0 1 3 4a1 1 0 0 1 1-1h3.5a1 1 0 0 1 1 1c0 1.25.2 2.45.57 3.57a1 1 0 0 1-.25 1z"/></svg>03-4120-7752</dd>
    <dt>緑が丘校</dt>
    <dd><svg width="14" height="14" viewBox="0 0 24 24"><path fill="#6aa63c" d="M6.6 10.8a15 15 0 0 0 6.6 6.6l2.2-2.2a1 1 0 0 1 1-.25 11.4 11.4 0 0 0 3.6.57 1 1 0 0 1 1 1V20a1 1 0 0 1-1 1A17 17 0 0 1 3 4a1 1 0 0 1 1-1h3.5a1 1 0 0 1 1 1c0 1.25.2 2.45.57 3.57a1 1 0 0 1-.25 1z"/></svg>04-6093-2214</dd>
  </dl>
  <ul class="side-nav">
    <li>トバキッチンについて</li>
    <li>入会案内</li>
    <li>コース案内</li>
    <li>料金表</li>
    <li>よくあるご質問</li>
    <li>教室案内</li>
  </ul>
  <div class="side-btn"><span class="dot"></span>お問い合わせ</div>
  <div class="side-btn"><span class="dot"></span>企業の方はこちら</div>
</aside>

<div class="sec-head" style="left:197px;top:288px;width:296px">新着情報</div>
<ul class="news">
  <li><time>2014年2月5日</time><span>春のコース一覧を更新しました</span></li>
  <li><time>2014年2月3日</time><span>本町校 体験レッスン日程のお知らせ</span></li>
  <li><time>2014年1月28日</time><span>港町校 パンコース新設のご案内</span></li>
  <li><time>2014年1月20日</time><span>緑が丘校 見学会を開催します</span></li>
  <li><time>2014年1月15日</time><span>年始休業期間のお知らせ</span></li>
</ul>
<div class="more" style="left:455px;top:448px">一覧へ ›</div>

<div class="sec-head" style="left:506px;top:288px;width:240px">今月のレシピ</div>
<div class="recipes">
  <div class="recipe"><div class="photo" role="img" aria-label="今月のレシピ料理写真"></div><span>季節の煮込み料理です。手軽に作れる一品をご紹介します。</span></div>
  <div class="recipe"><div class="photo" role="img" aria-label="今月のレシピ料理写真"></div><span>彩り野菜のサラダです。ドレッシングも手作りで楽しめます。</span></div>
  <div class="recipe"><div class="photo" role="img" aria-label="今月のレシピ料理写真"></div><span>焼き菓子のレシピです。おもてなしにもぴったりです。</span></div>
</div>

<div class="sec-head" style="left:197px;top:484px;width:549px">トバキッチンについて</div>
<div class="cards">
  <div class="card"><div class="photo" role="img" aria-label="野菜と食材の写真" style="background:linear-gradient(135deg,#c8d67a,#d8543a)"></div><h3>トバキッチンの特徴</h3><p>少人数制で一人ひとりに丁寧に指導します。</p></div>
  <div class="card"><div class="photo" role="img" aria-label="盛り付けた家庭料理の写真" style="background:linear-gradient(135deg,#f3e7c8,#c79a54)"></div><h3>レギュラーコース</h3><p>基本から学べる家庭料理のコースです。</p></div>
  <div class="card"><div class="photo" role="img" aria-label="洋菓子の写真" style="background:linear-gradient(135deg,#e8d9c0,#a9763f)"></div><h3>専門・特別コース</h3><p>本格的な料理やお菓子を学べます。</p></div>
  <div class="card"><div class="photo" role="img" aria-label="和菓子の写真" style="background:linear-gradient(135deg,#e6c5a6,#a85a3a)"></div><h3>短期集中コース</h3><p>短期間で基礎をしっかり身につけます。</p></div>
  <div class="card"><div class="photo" role="img" aria-label="焼きたてのピザの写真" style="background:linear-gradient(135deg,#e9b56a,#a33d22)"></div><h3>サンデーコース</h3><p>休日に気軽に参加できるコースです。</p></div>
  <div class="card"><div class="photo" role="img" aria-label="料理を学ぶ男性の手元の写真" style="background:linear-gradient(135deg,#f2f2ee,#b9b4aa)"></div><h3>男性コース</h3><p>初心者の男性も楽しく学べます。</p></div>
</div>

<div class="pagetop">▲ PAGETOP</div>

<footer class="site-footer">
  <div class="footer-brand brand" style="left:40px;top:40px">
    <span class="brand-mark"></span>
    <div><div class="brand-name">トバキッチン</div><div class="brand-sub">TOBA KITCHEN SCHOOL</div></div>
  </div>
  <div class="home-btn">HOME</div>
  <div class="footer-nav">
    <ul><li>トバキッチンについて</li><li>入会案内</li><li>コース案内</li></ul>
    <ul><li>料金表</li><li>よくあるご質問</li><li>教室案内</li></ul>
    <ul><li>プライバシーポリシー</li><li>サイトマップ</li><li>お問い合わせ</li></ul>
  </div>
  <div class="copyright">Copyright © 2014 TOBA KITCHEN SCHOOL All Rights Reserved.</div>
</footer>

</body>
</html>
```